Business Card Design for Event Planning Company

Create a business card for event planning company using our new logo. After I pick the design, I will need files made for 6 employees. Our company provides event design & logistics services as well as venue management. The font should be sans serif and complementary to the logo. I will need to know the name of the font selected for the final design. The phone numbers listed should be separated by "." not "-"

Address for the card
PO Box 318, Washington, DC 20019

Card One
Lorna Pettibone
lpettibone@galavoyant.com
202.481.7730

Card Two
Miriam Okonkwo
mokonkwo@galavoyant.com
202.556.2047

Card Three
Tessa Varnholt
tvarnholt@galavoyant.com
978.620.4471

Card Four
Robin Fess
rfess@galavoyant.com
202.718.3362

Card Five
Ada-Rose Pelletan-Uzor
adarose@galavoyant.com
202.839.1205

Card Six
Beatrix Holloway
Beatrix@galavoyant.com
202.492.6618

Target Market(s)

Corporate/Non-Profit

Industry/Entity Type

Event Planning

Contact Information for Business Card

Address for the card

Card One
Lorna Pettibone
lpettibone@galavoyant.com
202.481.7730

Card Two
Miriam Okonkwo
202.556.2047

Card Three
Tessa Varnholt
978.620.4471

Card Four
Robin Fess
rfess@galavoyant.com
202.718.3362

Card Five
Ada-Rose Pelletan-Uzor
202.839.1205

Card Six
Beatrix Holloway
202.492.6618

Font styles to use
Sans Serif

Colors

Designer to choose colors to be used in the design.

Requirements
Must have
• Two-sided with logo
Should not have
• Extra colors or be too busy

```html
<!DOCTYPE html>
<html lang="en">
<head>
<meta charset="utf-8">
<title>Galavoyant Business Card</title>
<link rel="stylesheet" href="https://fonts.googleapis.com/css2?family=Montserrat:wght@300;400;700&display=swap">
<style>
  :root {
    --teal: #5fa5a3;
    --ink: #0b0b0b;
    --paper: #ffffff;
    --stage: #d9d9d9;
  }
  * { margin: 0; padding: 0; box-sizing: border-box; }
  html, body { width: 1200px; height: 910px; overflow: hidden; }
  body {
    background: var(--stage);
    font-family: "Montserrat", sans-serif;
    position: relative;
  }
  .card {
    position: absolute;
    width: 560px;
    height: 320px;
    background: var(--paper);
    overflow: hidden;
    box-shadow: 0 6px 18px rgba(0,0,0,0.18);
  }
  .card-front { left: 60px; top: 60px; }
  .card-back { left: 580px; top: 530px; }
  .card-shapes { position: absolute; inset: 0; width: 100%; height: 100%; }
  .brand {
    position: absolute;
    display: flex;
    align-items: center;
    gap: 10px;
    color: var(--teal);
    font-weight: 300;
    letter-spacing: 0.5px;
    white-space: nowrap;
  }
  .brand-dot {
    display: block;
    border-radius: 50%;
    background: var(--teal);
  }
  .card-front .brand { left: 120px; top: 150px; font-size: 46px; }
  .card-front .brand-dot { width: 30px; height: 30px; }
  .card-back .brand { left: 30px; top: 70px; font-size: 28px; }
  .card-back .brand-dot { width: 19px; height: 19px; }
  .holder {
    position: absolute;
    right: 20px;
    top: 46px;
    color: var(--paper);
    font-weight: 700;
    font-size: 22px;
    text-align: right;
    white-space: nowrap;
  }
  .contact-list {
    position: absolute;
    right: 22px;
    bottom: 30px;
    list-style: none;
    color: var(--paper);
    font-size: 12px;
    font-weight: 400;
    text-align: right;
  }
  .contact-list li {
    display: flex;
    justify-content: flex-end;
    align-items: center;
    gap: 8px;
    margin-top: 9px;
    white-space: nowrap;
  }
  .contact-icon {
    width: 15px;
    height: 15px;
    display: block;
    flex: none;
  }
</style>
</head>
<body>

<section class="card card-front" aria-label="Card front">
  <svg class="card-shapes" viewBox="0 0 560 320" aria-hidden="true">
    <polygon points="356,0 560,0 560,250" fill="var(--teal)"/>
    <polygon points="0,0 356,0 560,250 560,292 340,22 0,22" fill="var(--ink)"/>
  </svg>
  <div class="brand"><span class="brand-dot"></span>galavoyant</div>
</section>

<section class="card card-back" aria-label="Card back">
  <svg class="card-shapes" viewBox="0 0 560 320" aria-hidden="true">
    <polygon points="362,14 560,14 560,320 183,320" fill="var(--teal)"/>
    <polygon points="325,0 560,0 560,14 362,14 183,320 145,320" fill="var(--ink)"/>
  </svg>
  <div class="brand"><span class="brand-dot"></span>galavoyant</div>
  <h1 class="holder">Lorna Pettibone</h1>
  <ul class="contact-list">
    <li>202.481.7730
      <svg class="contact-icon" viewBox="0 0 15 15" aria-label="Phone"><rect width="15" height="15" rx="2" fill="var(--paper)"/><path d="M4 3.5 L6 3.5 L6.6 5.6 L5.6 6.4 Q6.6 8.6 8.6 9.4 L9.4 8.4 L11.5 9 L11.5 11 Q7 11.5 4 6.5 Z" fill="var(--teal)"/></svg>
    </li>
    <li>lpettibone@galavoyant.com
      <svg class="contact-icon" viewBox="0 0 15 15" aria-label="Email"><rect width="15" height="15" rx="2" fill="var(--paper)"/><circle cx="7.5" cy="7.5" r="4.5" fill="none" stroke="var(--teal)" stroke-width="1.3"/><circle cx="7.5" cy="7.5" r="1.7" fill="none" stroke="var(--teal)" stroke-width="1.2"/></svg>
    </li>
    <li>PO Box 318, Washington, DC 20019
      <svg class="contact-icon" viewBox="0 0 15 15" aria-label="Mail"><rect width="15" height="15" rx="2" fill="var(--paper)"/><rect x="3" y="4.5" width="9" height="6" fill="none" stroke="var(--teal)" stroke-width="1.2"/><path d="M3 4.5 L7.5 8 L12 4.5" fill="none" stroke="var(--teal)" stroke-width="1.2"/></svg>
    </li>
  </ul>
</section>

</body>
</html>
```